Brochure DESIGN
QVB TRAVEL CHARTER COMPANY
Thanks A lot.
I ask this because I cann't open documents in .docx only .doc ~ In these circumstances I might retire, however I see no reaction to the first proposal !! :|
PLEASE USE PROJECT INFORMATION FOR DOCUMENT WORDS
please use info we've down loaded..
hello ! please post text what want you in .doc format ~ thanks
PLEASE REMEMBER TO TAKE OFF THE WORDS "SUNWARD TRIPS" FROM THE RED BUS, AND IF POSSIBLE, PLEASE FILL IN ANY RED OR TOUCH UP SPOTS ON THE BUS..
OTHER WISE, LOVE YOUR IDEAS..

```html
<!DOCTYPE html>
<html lang="en">
<head>
<meta charset="utf-8">
<title>QVB Travel Charter Company – Brochure</title>
<link href="https://fonts.googleapis.com/css2?family=Arimo:ital,wght@0,400;0,700;1,700&display=swap" rel="stylesheet">
<style>
  :root {
    --sky-top: #2f7fd6;
    --sky-mid: #8fc3ee;
    --sky-low: #dfeefa;
    --hill: #6c8f4a;
    --grass: #7fb63a;
    --grass-deep: #4f8a22;
    --panel: rgba(255, 255, 255, 0.72);
    --panel-edge: rgba(255, 255, 255, 0.9);
    --ink: #2b2b2b;
    --ink-soft: #3d3d3d;
    --accent: #d6171d;
    --bus-red: #c4161c;
    --bus-dark: #2a2a2e;
  }
  * { box-sizing: border-box; margin: 0; padding: 0; }
  html, body { width: 1200px; height: 679px; overflow: hidden; background: #fff; }
  body { font-family: "Arimo", Arial, sans-serif; color: var(--ink); }

  .brochure { position: relative; width: 1200px; height: 679px; overflow: hidden; }

  .landscape {
    position: absolute; inset: 0;
    background:
      linear-gradient(180deg, transparent 0, transparent 62%, var(--hill) 66%, var(--grass) 74%, var(--grass-deep) 100%),
      linear-gradient(180deg, var(--sky-top) 0%, var(--sky-mid) 35%, var(--sky-low) 60%);
  }

  .panel {
    position: absolute;
    background: var(--panel);
    border: 1px solid var(--panel-edge);
    border-radius: 14px;
  }

  .section-title {
    display: flex; align-items: center; gap: 12px;
    font-style: italic; font-weight: 700; font-size: 27px; line-height: 30px;
    white-space: nowrap; color: var(--ink);
    padding-left: 10px; margin-bottom: 10px;
  }
  .section-title::before {
    content: ""; width: 22px; height: 13px; background: var(--accent); flex: none;
  }

  .list { list-style: none; font-size: 12.5px; line-height: 20px; color: var(--ink-soft); padding: 0 18px 0 22px; }
  .list.bullets { font-size: 11.5px; line-height: 15px; text-transform: uppercase; }
  .list.bullets li { margin-bottom: 9px; }
  .list.bullets li::before { content: "• "; }

  .pricing  { left: 24px; top: 91px;  width: 326px; height: 173px; padding-top: 16px; }
  .features { left: 24px; top: 279px; width: 326px; height: 146px; padding-top: 10px; }
  .features .section-title { margin-bottom: 6px; }
  .note     { left: 24px; top: 439px; width: 326px; height: 173px; padding-top: 12px; }

  .contact {
    left: 439px; top: 439px; width: 324px; height: 173px;
    text-align: center; font-size: 17px; line-height: 1.4; color: var(--ink);
    padding-top: 22px;
  }
  .contact .hours { margin-top: 14px; }

  .brand-mark {
    position: absolute; display: flex; align-items: center; gap: 10px;
    font-weight: 700; color: #fff; letter-spacing: 0.5px; line-height: 1.15;
  }
  .brand-mark .dot { width: 14px; height: 14px; background: currentColor; flex: none; }
  .brand-mark.center { left: 470px; top: 370px; width: 260px; font-size: 17px; }

  .cover { left: 828px; top: 96px; width: 348px; height: 168px; text-align: center; padding: 38px 20px 0; }
  .cover .brand-mark { position: static; justify-content: center; color: var(--bus-red); font-size: 22px; }
  .cover .web { margin-top: 22px; font-size: 13px; color: var(--ink); }

  .coach {
    position: absolute; left: 820px; top: 340px; width: 380px; height: 339px;
    background: linear-gradient(180deg, var(--bus-dark) 0 30%, var(--bus-red) 30% 78%, var(--bus-dark) 78% 100%);
    border-radius: 40px 0 0 18px;
  }
</style>
</head>
<body>
  <main class="brochure">
    <div class="landscape" role="img" aria-label="Photo of blue sky with white clouds over green hills and a grassy meadow"></div>

    <section class="panel pricing">
      <h2 class="section-title">Pricing Information</h2>
      <ol class="list">
        <li>1. Pick up and drop off 15 miles or less $350</li>
        <li>2. $3.15 per mile per person</li>
        <li>3. 5 hours or less $575</li>
        <li>4. Day rates for 10 hours $795</li>
      </ol>
    </section>

    <section class="panel features">
      <h2 class="section-title">Features</h2>
      <ol class="list">
        <li>1. Restroom</li>
        <li>2. TV</li>
        <li>3. CD/DVD</li>
        <li>4. PA System</li>
      </ol>
    </section>

    <section class="panel note">
      <h2 class="section-title">NOTE</h2>
      <ul class="list bullets">
        <li>10% deposit with full payment before departure (non-refundable deposit if canceled)</li>
        <li>Bus insured $5,000,000.00</li>
        <li>SPAB certified</li>
      </ul>
    </section>

    <div class="brand-mark center"><span class="dot"></span><span>QVB TRAVEL CHARTER COMPANY</span></div>

    <section class="panel contact">
      <p>TEL: 310-555-0142</p>
      <p>FAX 310-555-0178</p>
      <p>www.qvbtravelcharter.com</p>
      <p class="hours">24-HOUR OPERATION</p>
      <p>4821 W. Harbor Ln. Carson, CA 90746</p>
    </section>

    <section class="panel cover">
      <div class="brand-mark"><span class="dot"></span><span>QVB TRAVEL CHARTER COMPANY</span></div>
      <p class="web">www.qvbtravelcharter.com</p>
    </section>

    <div class="coach" role="img" aria-label="Photo of a red and black charter coach bus"></div>
  </main>
</body>
</html>
```